International Trading Company, 'VOLA' needs a Business Card

The company name is "VOLA" and it has own logo design.
I'd like to use its logo on this business card.
I need two side Business Card.
I'll look forward to your great design.
Thank you very much in advance.

Contact Information for Business Card

Company Name : Vola Harbor Limited
Information Example
Tobias Wrenfold
Mobile(use icon please) : 1 (555) 014-2290
Tel(use icon please) : 1 (555) 014-6835
Email(use icon please) : tobias27@volaharbor.example
Address(use icon please) : 482 Larkmoor Rd, New York, NY 10199, USA

```html
<!DOCTYPE html>
<html lang="en">
<head>
<meta charset="utf-8">
<title>VOLA Business Card</title>
<link rel="stylesheet" href="https://fonts.googleapis.com/css2?family=Oswald:wght@500;600;700&family=Open+Sans:wght@600;700&display=swap">
<style>
  :root {
    --backdrop: #e9e8e6;
    --paper: #f7f7f6;
    --ink: #5c5c5e;
    --ink-dark: #4a4a4c;
    --grey-band: #7b7b7e;
    --grey-light: #d3d3d5;
    --grey-mid: #b9b9bc;
    --grey-deep: #717174;
    --white: #ffffff;
  }
  * { margin: 0; padding: 0; box-sizing: border-box; }
  html, body {
    width: 1200px;
    height: 1000px;
    overflow: hidden;
    background: var(--backdrop);
  }
  .canvas {
    position: relative;
    width: 1200px;
    height: 1000px;
  }
  .card {
    position: absolute;
    left: 200px;
    width: 800px;
    height: 457px;
    background: var(--paper);
    overflow: hidden;
    box-shadow: 0 6px 22px rgba(0,0,0,0.14);
  }
  .card--front { top: 30px; }
  .card--back { top: 513px; }
  .card__shapes {
    position: absolute;
    inset: 0;
    width: 100%;
    height: 100%;
  }
  .wordmark {
    position: absolute;
    font-family: "Oswald", sans-serif;
    font-weight: 700;
    line-height: 1;
    letter-spacing: 0.04em;
  }
  .card--front .wordmark {
    left: 42px;
    top: 58px;
    font-size: 58px;
    color: var(--ink-dark);
  }
  .holder-name {
    position: absolute;
    left: 300px;
    top: 232px;
    font-family: "Oswald", sans-serif;
    font-weight: 600;
    font-size: 50px;
    letter-spacing: 0.02em;
    color: var(--ink);
    text-transform: uppercase;
  }
  .contact-list {
    position: absolute;
    right: 62px;
    top: 30px;
    list-style: none;
    font-family: "Open Sans", sans-serif;
    font-weight: 700;
    font-size: 13px;
    color: var(--ink-dark);
  }
  .contact-list__item {
    display: flex;
    justify-content: flex-end;
    align-items: center;
    gap: 10px;
    height: 26px;
  }
  .contact-icon {
    width: 18px;
    height: 18px;
    flex: none;
  }
  .card--back .wordmark {
    left: 0;
    right: 0;
    top: 150px;
    text-align: center;
    font-size: 124px;
    color: var(--white);
    letter-spacing: 0.06em;
  }
  .back-email {
    position: absolute;
    left: 0;
    right: 0;
    top: 290px;
    text-align: center;
    font-family: "Open Sans", sans-serif;
    font-weight: 600;
    font-size: 15px;
    letter-spacing: 0.32em;
    color: var(--white);
  }
</style>
</head>
<body>
<main class="canvas">

  <section class="card card--front" aria-label="Business card front">
    <svg class="card__shapes" viewBox="0 0 800 457" aria-hidden="true">
      <polygon points="752,0 800,0 800,330 780,330" fill="var(--grey-light)"/>
      <polygon points="0,380 800,318 800,457 0,457" fill="var(--grey-band)"/>
      <polygon points="178,0 222,0 96,376 30,385" fill="var(--grey-light)"/>
      <polygon points="222,0 256,0 96,376" fill="var(--grey-mid)"/>
      <polygon points="0,385 30,385 96,376 0,457" fill="var(--grey-mid)"/>
    </svg>

    <div class="wordmark">VOLA</div>

    <ul class="contact-list">
      <li class="contact-list__item">
        <span>1 (555) 014-2290</span>
        <svg class="contact-icon" viewBox="0 0 18 18" aria-label="Mobile">
          <rect x="1" y="1" width="16" height="16" fill="none" stroke="var(--ink-dark)" stroke-width="1.5"/>
          <rect x="6" y="4" width="6" height="10" rx="1" fill="none" stroke="var(--ink-dark)" stroke-width="1.3"/>
        </svg>
      </li>
      <li class="contact-list__item">
        <span>1 (555) 014-6835</span>
        <svg class="contact-icon" viewBox="0 0 18 18" aria-label="Telephone">
          <rect x="1" y="1" width="16" height="16" fill="none" stroke="var(--ink-dark)" stroke-width="1.5"/>
          <path d="M5 4.5 L7 4.5 L8 7 L6.8 8 Q8 10.5 10 11.2 L11 10 L13.5 11 L13.5 13 Q8.5 13.5 5 8 Z" fill="var(--ink-dark)"/>
        </svg>
      </li>
      <li class="contact-list__item">
        <span>482 Larkmoor Rd, New York, NY 10199, USA</span>
        <svg class="contact-icon" viewBox="0 0 18 18" aria-label="Address">
          <rect x="1" y="1" width="16" height="16" fill="none" stroke="var(--ink-dark)" stroke-width="1.5"/>
          <path d="M9 14 Q5 9.5 5 7.5 A4 4 0 0 1 13 7.5 Q13 9.5 9 14 Z" fill="var(--ink-dark)"/>
          <circle cx="9" cy="7.5" r="1.4" fill="var(--paper)"/>
        </svg>
      </li>
      <li class="contact-list__item">
        <span>tobias27@volaharbor.example</span>
        <svg class="contact-icon" viewBox="0 0 18 18" aria-label="Email">
          <rect x="1" y="1" width="16" height="16" fill="none" stroke="var(--ink-dark)" stroke-width="1.5"/>
          <rect x="4" y="5.5" width="10" height="7" fill="none" stroke="var(--ink-dark)" stroke-width="1.3"/>
          <polyline points="4,5.5 9,9.5 14,5.5" fill="none" stroke="var(--ink-dark)" stroke-width="1.3"/>
        </svg>
      </li>
    </ul>

    <h1 class="holder-name">Tobias Wrenfold</h1>
  </section>

  <section class="card card--back" aria-label="Business card back">
    <svg class="card__shapes" viewBox="0 0 800 457" aria-hidden="true">
      <polygon points="0,0 640,0 800,380 800,457 560,457 0,290" fill="var(--grey-deep)"/>
    </svg>
    <div class="wordmark">VOLA</div>
    <p class="back-email">tobias27@volaharbor.example</p>
  </section>

</main>
</body>
</html>
```